Corvane Holdings , new business card design

investment firm with corporate clients . need double sided business card , vertical and horizontal options ,logo must be clear. prefer pantone colors only and sharp design. website also www.corvane-demo.ae

Khalid Bin Rashed
Managing Director
Tel. +971 4 000 1234
Mobile +971 50 000 5678
khalid@corvane-demo.ae
Palmgate Tower, officw 18-B07, Noor Terraces, Dubai

Khalid Bin Rashed
Managing Director

Serif

Designer to choose colors to be used in the design.

```html
<!DOCTYPE html>
<html lang="en">
<head>
<meta charset="utf-8">
<title>Corvane Holdings — Business Card</title>
<link href="https://fonts.googleapis.com/css2?family=Jost:ital,wght@0,300;0,400;0,500;1,400&display=swap" rel="stylesheet">
<style>
  :root {
    --brand-blue: #466f96;
    --brand-blue-dark: #2f5f8f;
    --ink: #3a3a3a;
    --paper: #ffffff;
    --backdrop: #e9ebee;
  }
  * { margin: 0; padding: 0; box-sizing: border-box; }
  html, body { width: 1200px; height: 963px; overflow: hidden; }
  body {
    background: var(--backdrop);
    font-family: "Jost", "Futura", sans-serif;
    position: relative;
  }
  .card {
    position: absolute;
    left: 320px;
    width: 560px;
    height: 320px;
    border-radius: 16px;
    overflow: hidden;
    box-shadow: 0 6px 18px rgba(0,0,0,0.15);
  }
  .card--front { top: 110px; background: var(--paper); }
  .card--back  { top: 530px; background: var(--brand-blue); }

  .wordmark {
    position: absolute;
    font-weight: 300;
    letter-spacing: 0.22em;
    text-transform: uppercase;
    white-space: nowrap;
  }
  .card--front .wordmark {
    left: 44px; top: 38px;
    font-size: 26px;
    color: var(--ink);
  }
  .card--back .wordmark {
    left: 50%; top: 50%;
    transform: translate(-50%, -50%);
    font-size: 38px;
    color: var(--paper);
  }

  .address {
    position: absolute;
    left: 44px; top: 128px;
    font-size: 15px;
    font-style: italic;
    line-height: 1.3;
    color: var(--ink);
  }
  .divider {
    position: absolute;
    left: 32px; top: 200px;
    width: 480px; height: 1px;
    background: var(--brand-blue-dark);
  }
  .person {
    position: absolute;
    right: 48px; top: 166px;
    text-align: right;
  }
  .person__name {
    font-size: 19px;
    font-weight: 400;
    letter-spacing: 0.02em;
    text-transform: uppercase;
    color: var(--brand-blue-dark);
    line-height: 1.2;
  }
  .person__title {
    margin-top: 12px;
    font-size: 15px;
    font-style: italic;
    color: var(--ink);
  }
  .contacts {
    position: absolute;
    left: 34px; top: 214px;
    list-style: none;
    font-size: 15px;
    line-height: 1.35;
    color: var(--ink);
  }
  .contacts li { display: flex; align-items: center; gap: 8px; }
  .contacts svg { width: 10px; height: 10px; flex: none; }
  .edge-tab {
    position: absolute;
    right: 0; top: 188px;
    width: 16px; height: 36px;
    background: var(--brand-blue-dark);
  }
</style>
</head>
<body>
  <section class="card card--front" aria-label="Business card front">
    <div class="wordmark">Corvane Holdings</div>

    <p class="address">Palmgate Tower, officw 18-B07,<br>Noor Terraces, Dubai</p>

    <div class="person">
      <p class="person__name">Khalid Bin Rashed</p>
      <p class="person__title">Managing Director</p>
    </div>

    <div class="divider"></div>

    <ul class="contacts">
      <li>
        <svg viewBox="0 0 10 10" aria-hidden="true"><path d="M2 1 L4 1 L4.6 3 L3.4 3.8 Q4.4 5.8 6.2 6.6 L7 5.4 L9 6 L9 8 Q5 9 2.5 6 Q1 4 2 1Z" fill="#2f5f8f"/></svg>
        +971 4 000 1234
      </li>
      <li>
        <svg viewBox="0 0 10 10" aria-hidden="true"><rect x="2.5" y="0.5" width="5" height="9" rx="1" fill="none" stroke="#2f5f8f"/><rect x="4.3" y="7.4" width="1.4" height="1" fill="#2f5f8f"/></svg>
        +971 50 000 5678
      </li>
      <li>
        <svg viewBox="0 0 10 10" aria-hidden="true"><rect x="0.5" y="2" width="9" height="6" fill="none" stroke="#2f5f8f"/><path d="M0.5 2 L5 5.5 L9.5 2" fill="none" stroke="#2f5f8f"/></svg>
        khalid@corvane-demo.ae
      </li>
    </ul>

    <div class="edge-tab"></div>
  </section>

  <section class="card card--back" aria-label="Business card back">
    <div class="wordmark">Corvane Holdings</div>
  </section>
</body>
</html>
```